Lumen Path - Fiber Internet to the home postcard

Design a postcard for my company, Lumen Path, using the logo below. On the front of the card:
- No Buffering • No BS
- Second line should be the logo
- $60 / month • 10-Gigs
- lumenpath.net

Color palate should follow the colors in the logo.

Address should say
- Special pricing during construction
- Our best price
- Our fastest speed
- $60 / month • 10-Gigs
- lumenpath.net

Target Market(s)

25 - 55 year olds. Middle income/class. People with kids and pick up trucks

Industry/Entity Type

Fiber Internet Service Provider

Font styles to use
Sans Serif

Colors

Designer to choose colors to be used in the design.

Requirements
Nice to have
• I am open to more creative changes

```html
<!DOCTYPE html>
<html lang="en">
<head>
<meta charset="utf-8">
<title>Lumen Path – Fiber Postcard</title>
<link href="https://fonts.googleapis.com/css2?family=Heebo:wght@300;400;500;700;800&display=swap" rel="stylesheet">
<style>
  :root {
    --navy: #1c2b5a;
    --deep-navy: #0f2458;
    --green: #7ac143;
    --green-dark: #5ea22f;
    --paper: #f8fbf6;
    --white: #ffffff;
  }
  * { margin: 0; padding: 0; box-sizing: border-box; }
  html, body { width: 1200px; height: 1200px; overflow: hidden; }
  body {
    background: var(--navy);
    font-family: "Heebo", Arial, sans-serif;
    position: relative;
  }
  .card {
    position: absolute;
    left: 215px;
    width: 750px;
    height: 510px;
    background: var(--paper);
    overflow: hidden;
  }
  .card--front { top: 92px; }
  .card--back { top: 639px; }

  .front__field {
    position: absolute; left: 0; top: 0;
    width: 750px; height: 372px;
    background: var(--green);
  }
  .edge { position: absolute; left: 0; }
  .front__edge { top: 340px; width: 750px; height: 40px; }

  .headline {
    position: absolute; left: 0; right: 0; top: 44px;
    text-align: center;
    color: var(--white);
    font-weight: 700;
    font-size: 50px;
    letter-spacing: -0.8px;
    line-height: 1.2;
  }
  .mascot {
    position: absolute;
    background: linear-gradient(180deg, var(--deep-navy) 0%, rgba(15,36,88,0.35) 100%);
    border-radius: 48px 48px 8px 8px;
  }
  .front__mascot { left: 240px; top: 118px; width: 100px; height: 215px; }

  .price-badge {
    position: absolute; left: 330px; top: 148px;
    width: 186px; height: 186px;
    border-radius: 50%;
    background: var(--deep-navy);
    text-align: center;
    line-height: 1;
  }
  .price-badge__speed {
    display: block; margin-top: 18px;
    color: var(--green); font-weight: 700; font-size: 70px; letter-spacing: -4px;
  }
  .price-badge__unit {
    display: block; margin-top: -4px;
    color: var(--white); font-weight: 700; font-size: 37px; letter-spacing: -0.5px;
  }
  .price-badge__rate {
    display: block; margin-top: 0;
    color: var(--white); font-weight: 700; font-size: 30px; letter-spacing: -1px;
  }
  .price-badge__rate em { font-style: normal; color: var(--green); }

  .brand {
    position: absolute;
    display: flex; align-items: center; gap: 14px;
    color: var(--deep-navy);
    font-weight: 800;
    letter-spacing: -1px;
    line-height: 1;
  }
  .brand__dot { border-radius: 50%; background: var(--green); flex: none; }
  .front__brand { left: 0; right: 0; justify-content: center; top: 405px; font-size: 66px; }
  .front__brand .brand__dot { width: 62px; height: 62px; }

  .back__brand { left: 52px; top: 52px; font-size: 56px; }
  .back__brand .brand__dot { width: 54px; height: 54px; }

  .back__panel {
    position: absolute; left: 0; top: 142px;
    width: 503px; height: 300px;
    background: var(--green);
  }
  .back__edge { top: 418px; width: 503px; height: 32px; }
  .back__heading {
    position: absolute; left: 51px; top: 160px;
    color: var(--white); font-weight: 400; font-size: 26px; letter-spacing: -0.6px;
    line-height: 1.2;
  }
  .back__mascot { left: 52px; top: 206px; width: 150px; height: 196px; }
  .perks {
    position: absolute; left: 214px; top: 222px;
    list-style: none;
    color: var(--white); font-weight: 400; font-size: 24px; letter-spacing: -0.6px;
  }
  .perks li { display: flex; align-items: center; gap: 10px; height: 30px; }
  .perks svg { width: 22px; height: 18px; flex: none; }
</style>
</head>
<body>

<section class="card card--front">
  <div class="front__field"></div>
  <svg class="edge front__edge" viewBox="0 0 750 40" preserveAspectRatio="none" aria-hidden="true">
    <path d="M0 18 C250 4 500 4 750 16 L750 40 L0 40 Z" fill="var(--paper)"/>
  </svg>

  <h1 class="headline">No Buffering. No B.S...</h1>
  <div class="mascot front__mascot" role="img" aria-label="Illustrated mascot figure pointing at the price badge"></div>

  <div class="price-badge">
    <span class="price-badge__speed">10</span>
    <span class="price-badge__unit">Gigs</span>
    <span class="price-badge__rate"><em>$60</em>/mth</span>
  </div>

  <div class="brand front__brand"><span class="brand__dot"></span>Lumen Path</div>
</section>

<section class="card card--back">
  <div class="brand back__brand"><span class="brand__dot"></span>Lumen Path</div>

  <div class="back__panel"></div>
  <svg class="edge back__edge" viewBox="0 0 503 32" preserveAspectRatio="none" aria-hidden="true">
    <path d="M0 14 C170 2 340 2 503 12 L503 32 L0 32 Z" fill="var(--paper)"/>
  </svg>

  <h2 class="back__heading">Special Pricing During Construction</h2>
  <div class="mascot back__mascot" role="img" aria-label="Illustrated mascot figure with raised arms and signal waves"></div>

  <ul class="perks">
    <li><svg viewBox="0 0 22 18"><path d="M2 10 L8 16 L20 3" fill="none" stroke="var(--deep-navy)" stroke-width="3.5"/></svg>Our best price</li>
    <li><svg viewBox="0 0 22 18"><path d="M2 10 L8 16 L20 3" fill="none" stroke="var(--deep-navy)" stroke-width="3.5"/></svg>Our fastest speed</li>
    <li><svg viewBox="0 0 22 18"><path d="M2 10 L8 16 L20 3" fill="none" stroke="var(--deep-navy)" stroke-width="3.5"/></svg>$60 / month • 10-Gigs</li>
    <li><svg viewBox="0 0 22 18"><path d="M2 10 L8 16 L20 3" fill="none" stroke="var(--deep-navy)" stroke-width="3.5"/></svg>lumenpath.net</li>
  </ul>
</section>

</body>
</html>
```